Kick-ass motivational company vision poster

We need a company poster that communicates our vision, and keeps us motivated when the going gets tough !

We want a cool graphic design that will stand the test of time, isn't cliched, and is something we're proud to hang around the office.

TEXT
No.1 provider of high quality software development resources in London.

We combine the best of local resourcing with access to a global network, that means we always deliver.

We want our staff to work in jobs they love, and in doing so, deliver fantastic customer service.

SIZE
A1 / A2 portrait

Target Market(s)

employees

Industry/Entity Type

Professional Service

Font styles to use
Sans Serif

Requirements
Must have
• a nice graphic design - appreciate that's pretty broad but we just want a cool design - doesn't necessarily have to match our corporate look and feel (www.quovanltd.com)
Should not have
• Cliche'd use of people / photos / fist punches / clip-art etc. (you get the idea)

```html
<!DOCTYPE html>
<html lang="en">
<head>
<meta charset="utf-8">
<title>Veltrix – Vision Poster</title>
<link rel="stylesheet" href="https://fonts.googleapis.com/css2?family=Fira+Sans:ital,wght@0,700;0,800;0,900;1,900&display=swap">
<style>
  :root {
    --navy-deep: #151e5a;
    --navy: #26348f;
    --royal: #3446b0;
    --orange: #e5801c;
    --silver-light: #f4f4f4;
    --silver-mid: #cfd2d6;
    --silver-dark: #6f7378;
    --text-light: #e8e8e8;
    --white: #ffffff;
  }
  * { margin: 0; padding: 0; box-sizing: border-box; }
  html, body { width: 848px; height: 1200px; overflow: hidden; background: var(--white); }
  .poster {
    position: relative;
    width: 848px;
    height: 1200px;
    overflow: hidden;
    font-family: "Fira Sans", Arial, sans-serif;
  }
  .backdrop {
    position: absolute; inset: 0;
    background:
      radial-gradient(circle at 768px 300px, var(--orange) 0 45px, rgba(229,128,28,0.55) 60px, rgba(229,128,28,0) 170px),
      radial-gradient(ellipse 560px 700px at 400px 560px, rgba(38,52,143,0) 55%, rgba(229,128,28,0.9) 100%),
      linear-gradient(180deg, var(--royal) 0%, var(--navy) 45%, var(--navy-deep) 52%, var(--navy) 70%, var(--royal) 100%);
  }
  .skyline {
    position: absolute;
    left: 0; top: 430px; width: 848px; height: 150px;
    background: linear-gradient(180deg, rgba(21,30,90,0) 0%, rgba(21,30,90,0.75) 55%, rgba(21,30,90,0.9) 100%);
  }
  .numeral {
    position: absolute;
    left: 250px; top: 10px;
    font-size: 700px; font-weight: 900; font-style: italic; line-height: 1;
    background: linear-gradient(160deg, var(--silver-light) 0%, var(--silver-mid) 55%, #e9eaec 100%);
    -webkit-background-clip: text; background-clip: text;
    color: transparent;
    filter: drop-shadow(2px -2px 0 var(--orange)) drop-shadow(-18px 12px 0 var(--silver-dark)) drop-shadow(4px 10px 10px rgba(0,0,0,0.5));
  }
  .label-no {
    position: absolute;
    left: 176px; top: 382px;
    font-size: 86px; font-weight: 800;
    color: var(--text-light);
    text-shadow: 3px 4px 6px rgba(0,0,0,0.55);
    letter-spacing: -1px;
  }
  .vision-line {
    position: absolute;
    left: 0; width: 848px; top: 652px;
    text-align: center;
    font-size: 72px; font-weight: 800; line-height: 82px;
    color: var(--text-light);
    text-shadow: 3px 4px 6px rgba(0,0,0,0.55);
  }
  .brand-tile {
    position: absolute;
    left: 612px; top: 1040px; width: 236px; height: 160px;
    background: var(--white);
    display: flex; align-items: center; justify-content: center;
  }
  .brand-name {
    font-size: 46px; font-weight: 700;
    color: var(--orange);
  }
</style>
</head>
<body>
  <main class="poster">
    <div class="backdrop" role="img" aria-label="Deep blue night sky with binary code streams, light rays and glowing orange sun"></div>
    <div class="skyline" role="img" aria-label="City skyline silhouette made of binary digits"></div>
    <div class="numeral" aria-hidden="true">1</div>
    <h1>
      <span class="label-no">No.</span>
      <span class="vision-line">provider of high<br>quality software<br>development<br>resources in London.</span>
    </h1>
    <div class="brand-tile">
      <span class="brand-name">veltrix</span>
    </div>
  </main>
</body>
</html>
```